BOOK COVER - LE CHEMIN DES BRUMES

I need a design for a book cover.
Title : LE CHEMIN DES BRUMES
Subtitle : Sous le ciel ocre
We are looking for a few ideas to pick from. Attached is a picture of the cover of the same book in English. This time, we want to do a French Edition but would like to use a crown as a silhouette with the sun rising inside of it - instead of the feather. We would also like to have the same concept of a white background. If you have another design idea, we are also open to it, but it just lets you know our style. We need the back and the spine designed as well. Photoshop is the preferred design program to use.
Trim size of the front cover is: 147mm x 210mm
Spine is: 12mm
PDF Text of the book is also attached which provides the bleed amount we need.
Writing for the back:
Le monde se trouve en plein combat. Les peuples sont victimes de guerres, l’amour et la compassion disparaissent. Y a-t-il une issue ?
Le Chemin des Brumes explique la situation actuelle du monde dans un con¬texte historique. Il explique le combat entre la vérité et le mensonge et dévoile la naissance du mal et les conséquences de ses pouvoirs sinistres.
Pas à pas, Le Chemin des Brumes dévoile le rétrécissement de notre liberté personnelle. C’est l’un des phénomènes les plus dangereux de notre temps. Voulez-vous reconnaître les pouvoirs qui se cachent derrière ces efforts ?
Le Chemin des Brumes pose un regard sur les problèmes essentiels et nous introduit derri-ère les coulisses de la politique mondiale. Il dévoile des faits passionnants et des pro-phéties concernant le futur. Il contient non seulement des révélations bouleversantes, mais également une vision encourageante de notre avenir.
Le Chemin des Brumes a été traduit en plus de 80 langues et lu par des millions de personnes. Vous tenez en main l’un des livres les plus importants au monde !
For selling/mass distribution/gifts during events

```html
<!DOCTYPE html>
<html lang="fr">
<head>
<meta charset="utf-8">
<title>Le Chemin des Brumes — couverture</title>
<link rel="stylesheet" href="https://fonts.googleapis.com/css2?family=Antonio:wght@400;500&family=Barlow+Condensed:ital,wght@0,700;1,700&family=Montserrat:wght@400&display=swap">
<style>
  :root {
    --stage: #262626;
    --paper: #ffffff;
    --ink: #1e1e1e;
    --ink-soft: #2a2a2a;
    --crown-dark: #3a2414;
    --crown-mid: #8a4a14;
    --sun: #ffd76a;
    --sun-core: #fff6d8;
  }
  * { box-sizing: border-box; margin: 0; padding: 0; }
  html, body {
    width: 1200px; height: 561px; overflow: hidden;
    background: var(--stage);
  }
  .cover-spread {
    position: absolute; left: 207px; top: 10px;
    width: 785px; height: 541px;
    background: var(--paper);
    overflow: hidden;
  }
  .cover-type {
    position: absolute; inset: 0;
    width: 785px; height: 541px;
  }
  .title-face { font-family: "Antonio", "Oswald", sans-serif; font-weight: 400; fill: var(--ink); }
  .subtitle-face { font-family: "Barlow Condensed", sans-serif; font-weight: 700; font-style: italic; fill: var(--ink-soft); }
  .author-face { font-family: "Barlow Condensed", sans-serif; font-weight: 700; fill: var(--ink); }

  .back-blurb {
    position: absolute; left: 27px; top: 168px; width: 324px;
    font-family: "Montserrat", sans-serif; font-size: 9.1px; line-height: 12.7px;
    color: var(--ink); text-align: justify; text-align-last: center;
  }
  .back-blurb p { margin-bottom: 12.7px; }

  .crown-art {
    position: absolute; left: 492px; top: 322px; width: 209px; height: 126px;
    border-radius: 6px 6px 40% 40% / 6px 6px 14px 14px;
    background:
      radial-gradient(ellipse 45% 40% at 50% 78%, var(--sun-core) 0%, var(--sun) 25%, rgba(255,170,40,0.6) 50%, transparent 75%),
      linear-gradient(180deg, var(--crown-dark) 0%, var(--crown-mid) 60%, var(--crown-dark) 100%);
  }
  .crown-shadow {
    position: absolute; left: 470px; top: 440px; width: 255px; height: 14px;
    background: radial-gradient(ellipse at center, rgba(0,0,0,0.35), transparent 70%);
  }
</style>
</head>
<body>
  <main class="cover-spread">
    <div class="crown-shadow"></div>
    <div class="crown-art" role="img" aria-label="Silhouette de couronne avec un soleil levant sur la Terre à l'intérieur"></div>

    <svg class="cover-type" viewBox="0 0 785 541" aria-hidden="false">
      <!-- back cover title -->
      <g class="back-title">
        <text class="title-face" x="125" y="90" font-size="34" textLength="16" lengthAdjust="spacingAndGlyphs">LE</text>
        <text class="title-face" x="148" y="90" font-size="64" textLength="106" lengthAdjust="spacingAndGlyphs">CHEMIN</text>
        <text class="title-face" x="120" y="136" font-size="51" textLength="139" lengthAdjust="spacingAndGlyphs">DES BRUMES</text>
        <text class="subtitle-face" x="133" y="158" font-size="19" textLength="114" lengthAdjust="spacingAndGlyphs">SOUS LE CIEL OCRE</text>
      </g>

      <!-- spine -->
      <g class="spine" transform="translate(392,0) rotate(90)">
        <text class="title-face" x="33" y="8.5" font-size="22" textLength="201" lengthAdjust="spacing">LE CHEMIN DES BRUMES</text>
        <text class="subtitle-face" x="248" y="7.5" font-size="21" textLength="116" lengthAdjust="spacingAndGlyphs">SOUS LE CIEL OCRE</text>
        <text class="author-face" x="389" y="7" font-size="20" textLength="132" lengthAdjust="spacing">MARTHE L. VIDAL</text>
      </g>

      <!-- front cover -->
      <g class="front-title">
        <text class="title-face" x="450" y="153" font-size="90" textLength="37" lengthAdjust="spacingAndGlyphs">LE</text>
        <text class="title-face" x="500" y="153" font-size="150" textLength="223" lengthAdjust="spacingAndGlyphs">CHEMIN</text>
        <text class="title-face" x="441" y="254" font-size="113" textLength="314" lengthAdjust="spacingAndGlyphs">DES BRUMES</text>
        <text class="subtitle-face" x="488" y="294" font-size="34" textLength="220" lengthAdjust="spacingAndGlyphs">SOUS LE CIEL OCRE</text>
        <text class="author-face" x="497" y="514" font-size="38" textLength="200" lengthAdjust="spacing">MARTHE L. VIDAL</text>
      </g>
    </svg>

    <section class="back-blurb">
      <p>Le monde se trouve en plein combat. Les peuples sont victimes de guerres, l’amour et la compassion disparaissent. Y a-t-il une issue ?</p>
      <p>Le Chemin des Brumes explique la situation actuelle du monde dans un contexte historique. Il explique le combat entre la vérité et le mensonge et dévoile la naissance du mal et les conséquences de ses pouvoirs sinistres.</p>
      <p>Pas à pas, Le Chemin des Brumes dévoile le rétrécissement de notre liberté personnelle. C’est l’un des phénomènes les plus dangereux de notre temps. Voulez-vous reconnaître les pouvoirs qui se cachent derrière ces efforts ?</p>
      <p>Le Chemin des Brumes pose un regard sur les problèmes essentiels et nous introduit derrière les coulisses de la politique mondiale. Il dévoile des faits passionnants et des prophéties concernant le futur. Il contient non seulement des révélations bouleversantes, mais également une vision encourageante de notre avenir.</p>
      <p>Le Chemin des Brumes a été traduit en plus de 80 langues et lu par des millions de personnes. Vous tenez en main l’un des livres les plus importants au monde !</p>
    </section>
  </main>
</body>
</html>
```